Beekeeper needs a label for honey jars

Ciao! I'm from Como Italy
I'm a hobbyist beekeeper and I produce honey for myself and my friends.
I've named my apiary "Dado di sole," a play on words between my nickname (Dado, from Edoardo) and the Italian expression "Dado di sole," which translates to "a drizzle of honey" in English.
I need to create a label for my honey glass jars (250 gr and 500 gr).
I don't need a label for commercial purposes. I would like to include at least the name “Apicoltura Dado di sole", the type of honey (e.g., wildflower, acacia...) and a space for the production year, to be handwritten each year.
In the design some references to the world of bees.
For reference, attached a label with a style I like
Attached are the images of the selected jars and their measurements
Thanks and good job!

beekeeping, honey

• I would like an elegant style with clean graphics.
• Predominance of black color.

```html
<!DOCTYPE html>
<html lang="en">
<head>
<meta charset="utf-8">
<title>Apicoltura Dado di sole – Honey Label</title>
<link rel="stylesheet" href="https://fonts.googleapis.com/css2?family=Gloock&family=Montserrat:wght@500;600&display=swap">
<style>
  :root {
    --backdrop: #e6d6b9;
    --label-paper: #ecebf1;
    --ink: #141414;
    --frame: #2a2a2a;
    --comb-tint: #cfced8;
  }
  html, body {
    margin: 0;
    padding: 0;
    width: 1200px;
    height: 1200px;
    overflow: hidden;
    background: var(--backdrop);
  }
  .canvas {
    position: relative;
    width: 1200px;
    height: 1200px;
  }
  .label {
    position: absolute;
    left: 100px;
    top: 165px;
    width: 1000px;
    height: 870px;
    background: var(--label-paper);
    color: var(--ink);
    overflow: hidden;
  }
  .label-frame {
    position: absolute;
    inset: 28px 26px 30px 26px;
    border: 2px solid var(--frame);
  }
  .comb-pattern {
    position: absolute;
    background: linear-gradient(to bottom, rgba(207,206,216,0) 0%, var(--comb-tint) 35%, var(--comb-tint) 75%, rgba(207,206,216,0.4) 100%);
    opacity: 0.75;
  }
  .comb-pattern.left { left: 8px; top: 230px; width: 150px; height: 620px; }
  .comb-pattern.right { right: 8px; top: 20px; width: 160px; height: 830px; }
  .comb-pattern.bottom-left { left: 150px; top: 720px; width: 180px; height: 130px; opacity: 0.5; }
  .comb-pattern.bottom-right { right: 160px; top: 740px; width: 180px; height: 110px; opacity: 0.5; }
  .seal {
    position: absolute;
    left: 440px;
    top: 110px;
    width: 120px;
    height: 120px;
  }
  .brand-name {
    position: absolute;
    left: 0;
    right: 0;
    top: 316px;
    margin: 0;
    text-align: center;
    font-family: "Gloock", serif;
    font-weight: 400;
    font-size: 98px;
    line-height: 134px;
    letter-spacing: 2px;
  }
  .honey-type {
    position: absolute;
    left: 0;
    right: 0;
    top: 588px;
    text-align: center;
    font-family: "Montserrat", sans-serif;
    font-weight: 500;
    font-size: 35px;
    letter-spacing: 3px;
  }
  .year-line {
    position: absolute;
    left: 338px;
    width: 324px;
    top: 714px;
    height: 4px;
    background: var(--ink);
  }
  .details {
    position: absolute;
    left: 0;
    right: 0;
    top: 734px;
    text-align: center;
    font-family: "Montserrat", sans-serif;
    font-weight: 500;
    font-size: 19px;
    line-height: 28px;
    letter-spacing: 1.5px;
  }
  .quality-marks {
    position: absolute;
    left: 780px;
    top: 748px;
    width: 160px;
    height: 76px;
  }
</style>
</head>
<body>
<div class="canvas">
  <section class="label">
    <div class="comb-pattern left" role="img" aria-label="Faint honeycomb pattern"></div>
    <div class="comb-pattern right" role="img" aria-label="Faint honeycomb pattern"></div>
    <div class="comb-pattern bottom-left" role="img" aria-label="Faint honeycomb pattern"></div>
    <div class="comb-pattern bottom-right" role="img" aria-label="Faint honeycomb pattern"></div>
    <div class="label-frame"></div>

    <svg class="seal" viewBox="0 0 120 120" aria-hidden="true">
      <circle cx="60" cy="60" r="56" fill="none" stroke="#141414" stroke-width="3"/>
    </svg>

    <h1 class="brand-name">APICOLTURA<br>DADO DI SOLE</h1>
    <div class="honey-type">WILDFLOWER HONEY</div>
    <div class="year-line" role="img" aria-label="Write-in line for the handwritten production year"></div>
    <div class="details">NO PRESERVATIVE<br>250 ML | 8.5 OZ</div>

    <svg class="quality-marks" viewBox="0 0 160 76" aria-hidden="true">
      <circle cx="38" cy="40" r="32" fill="none" stroke="#141414" stroke-width="2.5"/>
      <circle cx="118" cy="36" r="32" fill="none" stroke="#141414" stroke-width="2.5"/>
    </svg>
  </section>
</div>
</body>
</html>
```